Professional Website for Commercial Real Estate Broker

I own a small boutique commercial real estate company called Birchwell Holdings.
My current website is www.teamdurnio.com and is hosted on hostlark. I am looking for an all new website that will allow me to compete with bigger players in our industry. In other words, I need something professional, sleek, and functional.

I am looking for a designer that can take my complete website all the way to coding, migration, and launch. I understand that this may be an add'l charge, so please include with your design submission what the add'l charge will be to take the website to launch with all functionality as described below.

As an example of a page in my industry that I like please check out: www.marcusolverin.com.

My logo is attached and my main colors are the blue, white, grey - similar to the logo.

I am looking for a five page website with the following pages:

Home
Birchwell Team
Services
Sold Properties
Contact

A couple of features that I will want on the site are:

- I want to make sure that we can imbed a news commercial real estate news feed from: http://www.plazowire.com/news/ on the website's home page, similar to how it is on marcusolverin.com.

- Sold Properties page will allow me to upload the following information on to the website so that I can add new properties that I have recently sold on a weekly or monthly basis. I would like the information to be displayed similarly to http://www.marcusolverin.com/properties.html . I should be able to upload: picture, price, bldg size, lot size, closing date for each property. This will require a user friendly back end that I can navigate.

- On the home page, I also want to have a form where visitors can request a Market Analysis of their property by entering: Name, property address, email address, phone number. I will be sent an email with this information and I can follow up via telephone or email direct.

- The Birchwell Team page will have a picture, contact info, and brief bio for each member of the team. I would like to be able to adjust this on a user friendly back end.

I have included my Company Logo. Feel free to use any text from my current website: www.teamdurnio.com. Also, any sleek looking stock photos of office / commercial buildings can be used for the initial design purposes.

I look forward to getting your design submittal and moving forward asap!

Target Market(s)

Los Angeles real estate brokers, developers, and investors.

Industry/Entity Type

Real Estate

Coding

Coded - Design and coding required

Number of Pages Required

5+ page

Font styles to use
Sans Serif

Colors
ffffff
85abd2
0455a3
b2b2b2
000000
3276b5

Requirements
Must have
• Sleek and professional design.
• - I want to make sure that we can imbed a news commercial real estate news feed from: http://www.plazowire.com/news/ on the website's home page, similar to how it is on marcusolverin.com.
• - Sold Properties page will allow me to upload the following information on to the website so that I can add new properties that I have recently sold on a weekly or monthly basis. I would like the information to be displayed similarly to http://www.marcusolverin.com/properties.html . I should be able to upload: picture, price, bldg size, lot size, closing date for each property. This will require a user friendly back end that I can navigate.
• - On the home page, I also want to have a form where visitors can request a Market Analysis of their property by entering: Name, property address, email address, phone number. I will be sent an email with this information and I can follow up via telephone or email direct.
Nice to have
• Dynamic banner on the home page with beautiful photos that change every few seconds.

```html
<!DOCTYPE html>
<html lang="en">
<head>
<meta charset="utf-8">
<title>Birchwell Holdings — Commercial Real Estate</title>
<link href="https://fonts.googleapis.com/css2?family=Poppins:wght@300;400;500;600;700&display=swap" rel="stylesheet">
<style>
:root{
  --navy:#0b2a6b;
  --blue:#0455a3;
  --sky:#1f9be0;
  --mid:#3276b5;
  --pale:#85abd2;
  --grey:#b2b2b2;
  --light:#eceef0;
  --ink:#1b1b1b;
  --dark:#2b2f36;
  --white:#ffffff;
}
*{box-sizing:border-box;margin:0;padding:0}
html,body{width:1200px;height:4213px;overflow:hidden}
body{font-family:'Poppins',sans-serif;color:var(--ink);background:var(--white);position:relative}
.abs{position:absolute}
svg{display:block}

/* top bar */
.topbar{top:0;left:0;width:1200px;height:26px;background:#7a7d82;color:#eef;font-size:11px;display:flex;align-items:center;padding:0 150px}
.topbar span{margin-right:28px}
.topbar .social{margin-left:auto;display:flex;gap:14px}
.dot{width:10px;height:10px;border-radius:50%;background:#dfe6f2;display:inline-block}

/* nav */
.nav{top:26px;left:0;width:1200px;height:54px;background:var(--white)}
.brand{position:absolute;left:168px;top:14px;display:flex;align-items:center;gap:8px;color:var(--blue);font-weight:700;font-size:22px;letter-spacing:1px}
.brand i{width:22px;height:22px;background:var(--blue);display:block}
.menu{position:absolute;left:402px;top:19px;display:flex;gap:26px;font-size:12px;color:#555;text-transform:uppercase;white-space:nowrap}
.menu .on{color:var(--sky)}
.callbox{position:absolute;right:0;top:0;width:310px;height:54px;background:var(--navy);color:#fff;font-weight:600;font-size:22px;display:flex;align-items:center;padding-left:30px;gap:10px}

/* hero */
.hero{top:80px;left:0;width:1200px;height:552px;background:linear-gradient(180deg,#3c4f66 0%,#5c6a78 45%,#7a6a55 80%,#3a3a3c 100%)}
.slide-arrow{top:330px;color:#fff;font-size:34px;font-weight:300;line-height:1}
.dots{top:600px;left:570px;display:flex;gap:8px}
.dots i{width:9px;height:9px;border-radius:50%;background:#fff;opacity:.7;display:block}
.dots i:first-child{opacity:1;background:var(--sky)}
.analysis{top:163px;left:748px;width:309px;height:400px;background:var(--white);border:6px solid #cfd6de}
.analysis h3{background:var(--sky);color:#fff;font-weight:400;font-size:19px;line-height:1.3;padding:12px 24px}
.analysis .field{margin:14px 24px 0;border-bottom:1px solid #555;font-size:13px;color:#333;padding-bottom:6px}
.robot{margin:20px 24px 0;display:flex;align-items:center;gap:8px;font-size:14px}
.robot b{width:16px;height:16px;border:1px solid #333;display:block}
.btn{background:var(--sky);color:#fff;font-size:16px;display:inline-flex;align-items:center;gap:10px;padding:8px 20px}
.analysis .btn{margin:20px 24px 0}

/* find sold */
.find{top:632px;left:0;width:1200px;height:248px;background:linear-gradient(90deg,#0a2466,#0a4aa0)}
.find h2{position:absolute;left:110px;top:82px;color:#fff;font-size:34px;font-weight:700;line-height:1.1;text-align:right;width:210px}
.find .divider{position:absolute;left:350px;top:0;width:2px;height:248px;background:rgba(255,255,255,.25)}
.sel{position:absolute;height:34px;border:1px solid #fff;color:#fff;font-size:13px;display:flex;align-items:center;padding:0 10px;justify-content:space-between}
.sel::after{content:"▾";font-size:11px}
.sel.plain::after{content:""}
.range{position:absolute;color:#fff;font-size:13px}
.range .track{width:206px;height:3px;background:var(--sky);margin-top:8px;position:relative}
.range .track::before,.range .track::after{content:"";position:absolute;top:-5px;width:12px;height:12px;border-radius:50%;background:var(--sky)}
.range .track::before{left:-2px}.range .track::after{right:-2px}
.search{position:absolute;left:980px;top:793px;background:var(--sky);color:#fff;font-size:14px;padding:6px 16px}

/* about */
.about-img{top:880px;left:0;width:570px;height:380px;background:linear-gradient(180deg,#9fb4c8 0%,#6b7f90 45%,#3f5a46 80%,#2e3a30 100%)}
.about-text{top:935px;left:620px;width:450px;font-size:14px;line-height:2.05;color:#444}
.about-text .btn{margin-top:28px}

/* section heading */
.heading{position:absolute;left:160px;font-size:42px;font-weight:600;color:var(--ink);display:flex;align-items:center}
.heading em{font-style:normal;color:var(--sky);font-weight:300;margin-right:6px}
.heading::after{content:"";position:absolute;left:22px;bottom:-10px;width:78px;height:4px;background:var(--sky)}
.heading.light{color:#fff}
.pager{position:absolute;display:flex;align-items:center;gap:14px}
.pager .prev{color:#aaa;font-size:20px}
.pager .next{width:34px;height:34px;background:var(--sky);color:#fff;display:flex;align-items:center;justify-content:center}
.pager .all{background:var(--dark);color:#fff;font-size:14px;padding:8px 24px}

/* sold cards */
.card{position:absolute;top:1436px;width:264px}
.card .ph{height:146px}
.card h4{font-weight:400;font-size:17px;margin-top:12px}
.card .price{color:var(--sky);font-weight:600;font-size:19px;margin-top:8px}
.card .meta{font-size:11px;color:#555;margin-top:6px;display:flex;align-items:center;gap:6px;line-height:1.3}
.card .bar{margin-top:12px;height:36px;background:var(--sky);display:flex;color:#fff;font-size:11px;align-items:center}
.card .bar span{padding:0 8px;display:flex;align-items:center;gap:5px;height:100%}
.card .bar .go{margin-left:auto;background:var(--blue);width:56px;justify-content:center}

/* specialties */
.special{top:1852px;left:0;width:1200px;height:508px;background:linear-gradient(180deg,#1d2a44 0%,#2d4563 55%,#1a2a3e 100%)}
.special p{position:absolute;top:70px;left:0;width:1200px;text-align:center;color:#fff;font-size:17px;line-height:1.75}
.spec{position:absolute;top:238px;width:120px;text-align:center;color:#fff;font-size:15px}
.spec .ring{width:78px;height:78px;margin:0 auto 4px;border-radius:50%;background:var(--sky);border:4px solid #fff;display:flex;align-items:center;justify-content:center}

/* team */
.member{position:absolute;top:2549px;width:192px}
.member .ph{height:192px;background:linear-gradient(180deg,#7e8a94,#c4c8cc)}
.member.pick .ph{outline:10px solid var(--sky)}
.member h5{font-weight:400;font-size:21px;margin-top:18px}
.member h5 span{color:var(--sky)}
.member small{font-size:14px;color:#666}

/* news */
.news{top:2872px;left:0;width:1200px;height:711px;background:var(--light)}
.story{position:absolute;top:3043px;width:265px}
.story .ph{height:155px}
.story.pick .ph{outline:8px solid var(--sky)}
.story h6{font-size:16px;font-weight:600;line-height:1.4;margin-top:22px}
.story p{font-size:13px;color:#555;line-height:1.9;margin-top:14px}

/* contacts */
.contacts{top:3583px;left:0;width:1200px;height:630px;background:linear-gradient(180deg,#112a6a,#0b3a8a 60%,#0d2c6d)}
.inp{position:absolute;border:1.5px solid #fff;color:#fff;font-size:14px;padding:6px 8px;height:40px}
.info{position:absolute;left:725px;color:#fff;display:flex;align-items:center;gap:18px}
.footline{top:4103px;left:120px;width:960px;height:1px;background:rgba(255,255,255,.4)}
.copy{top:4128px;left:0;width:1200px;text-align:center;color:#fff;font-size:13px}
.fsocial{top:4130px;left:898px;display:flex;gap:24px}
</style>
</head>
<body>

<div class="abs topbar">
  <span>▪ English</span><span>Contact</span><span>✉ info@teamdurnio.com</span>
  <div class="social"><i class="dot"></i><i class="dot"></i><i class="dot"></i><i class="dot"></i><i class="dot"></i></div>
</div>

<header class="abs nav">
  <div class="brand"><i></i>BIRCHWELL</div>
  <nav class="menu"><span class="on">Home</span><span>Services</span><span>Sold Properties</span><span>Birchwell Team</span><span>Contact</span></nav>
  <div class="callbox">
    <svg width="20" height="20" viewBox="0 0 24 24"><path fill="#fff" d="M6.6 10.8a15 15 0 006.6 6.6l2.2-2.2a1 1 0 011-.25 11.4 11.4 0 003.6.57 1 1 0 011 1V20a1 1 0 01-1 1A17 17 0 013 4a1 1 0 011-1h3.5a1 1 0 011 1c0 1.25.2 2.45.57 3.6a1 1 0 01-.25 1z"/></svg>
    (424) 555-0182
  </div>
</header>

<section class="abs hero" role="img" aria-label="Night view of a city skyline with lit downtown towers and streets"></section>
<div class="abs slide-arrow" style="left:48px">‹</div>
<div class="abs slide-arrow" style="left:1128px">›</div>
<div class="abs dots"><i></i><i></i><i></i><i></i><i></i></div>

<form class="abs analysis">
  <h3>Request Market Analysis For Your Property</h3>
  <div class="field">Your Name</div>
  <div class="field">Property Address</div>
  <div class="field">Email</div>
  <div class="field">Phone Number</div>
  <div class="robot"><b></b>I am not a robot</div>
  <div class="btn">Request
    <svg width="16" height="14" viewBox="0 0 16 14"><path fill="#fff" d="M0 6l16-6-3 14-5-4-2 3V9l7-6-9 5z"/></svg>
  </div>
</form>

<section class="abs find">
  <h2>FIND SOLD PROPERTIES</h2>
  <div class="divider"></div>
  <div class="sel" style="left:400px;top:60px;width:208px">For Sale or Lease</div>
  <div class="sel" style="left:632px;top:60px;width:208px">All Property Types</div>
  <div class="sel" style="left:862px;top:60px;width:208px">By Price</div>
  <div class="sel plain" style="left:400px;top:104px;width:208px">City</div>
  <div class="sel" style="left:632px;top:104px;width:208px">All States/Provinces</div>
  <div class="sel" style="left:862px;top:104px;width:98px">Min Price</div>
  <div class="sel" style="left:972px;top:104px;width:98px">Max Price</div>
  <div class="range" style="left:400px;top:148px">Size [0 - 1,000] SqFt<div class="track"></div></div>
  <div class="range" style="left:632px;top:148px">Land Area [0 - 1,000] SqFt<div class="track"></div></div>
</section>
<div class="search">⌕ Search</div>

<div class="abs about-img" role="img" aria-label="Aerial view of high-rise towers beside a large green park"></div>
<div class="abs about-text">
  Birchwell Holdings is a commercial real estate brokerage firm that provides a range of services to assist each of our clients in reaching their real estate objectives quickly and efficiently. Our focus on Southern California investment properties allows us to have a unique and focused perspective on this highly competitive market. Through our experience, diligence and resourcefulness, we help our clients make informed real estate decisions with their specific goals in mind.
  <br><div class="btn">Read More ›</div>
</div>

<h2 class="heading" style="top:1340px"><em>//</em>Sold Properties</h2>
<div class="pager" style="left:856px;top:1356px"><span class="prev">‹</span><span class="next">›</span><span class="all">View All</span></div>

<article class="card" style="left:160px">
  <div class="ph" role="img" aria-label="Single-storey house with garden" style="background:linear-gradient(180deg,#b9cbd9,#9a9a84)"></div>
  <h4>Single House Near Orlando</h4>
  <div class="price">$136,080</div>
  <div class="meta">◆ House</div>
  <div class="meta">● Orlando Park IL 60485, Chicago IL</div>
  <div class="meta">▦ October 12, 2017</div>
  <div class="bar"><span>▣ 12,000 SqFt</span><span>▤ 185 SqFt</span><span class="go">→</span></div>
</article>
<article class="card" style="left:466px">
  <div class="ph" role="img" aria-label="Open-plan office interior with red chairs" style="background:linear-gradient(180deg,#e3e5e8,#b7a9a9)"></div>
  <h4>Corporate Office</h4>
  <div class="price">$92,230</div>
  <div class="meta">◆ Office</div>
  <div class="meta">● Orlando Park IL 60485, Chicago IL</div>
  <div class="meta">▦ September 08, 2017</div>
  <div class="bar"><span>▣ 12,000 SqFt</span><span>▤ 185 SqFt</span><span class="go">→</span></div>
</article>
<article class="card" style="left:776px">
  <div class="ph" role="img" aria-label="White multi-storey industrial building" style="background:linear-gradient(180deg,#cfdbe6,#9aa3ab)"></div>
  <h4>Industrial Building</h4>
  <div class="price">$222,900</div>
  <div class="meta">◆ Industrial</div>
  <div class="meta">● Orlando Park IL 60485, Chicago IL</div>
  <div class="meta">▦ August 30, 2017</div>
  <div class="bar"><span>▣ 12,000 SqFt</span><span>▤ 185 SqFt</span><span class="go">→</span></div>
</article>

<section class="abs special" role="img" aria-label="Dusk aerial view of a dense city of towers">
  <p>Birchwell Holdings provides specialized<br>expertise in specific property types including:</p>
  <div class="spec" style="left:212px"><div class="ring"><svg width="40" height="40" viewBox="0 0 40 40"><path fill="#fff" d="M4 14h32v22H4zM8 6h24l4 8H4z"/><path fill="#1f9be0" d="M8 20h6v6H8zm9 0h6v6h-6zm9 0h6v6h-6zM16 30h8v6h-8z"/></svg></div>Retail</div>
  <div class="spec" style="left:333px"><div class="ring"><svg width="40" height="40" viewBox="0 0 40 40"><path fill="#fff" d="M4 36V16l9 6v-6l9 6v-6l9 6V6h5v30z"/></svg></div>Industrial</div>
  <div class="spec" style="left:471px"><div class="ring"><svg width="40" height="40" viewBox="0 0 40 40"><path fill="#fff" d="M8 4h24v32H8z"/><path fill="#1f9be0" d="M12 8h6v4h-6zm10 0h6v4h-6zM12 16h6v4h-6zm10 0h6v4h-6zM12 24h6v4h-6zm10 0h6v4h-6z"/></svg></div>Office</div>
  <div class="spec" style="left:603px"><div class="ring"><svg width="40" height="40" viewBox="0 0 40 40"><path fill="#fff" d="M6 36V12h10V4h8v8h10v24z"/><path fill="#1f9be0" d="M10 16h4v4h-4zm16 0h4v4h-4zM18 10h4v4h-4zm-8 14h4v4h-4zm16 0h4v4h-4zm-8-6h4v4h-4z"/></svg></div>Apartments</div>
  <div class="spec" style="left:724px"><div class="ring"><svg width="40" height="40" viewBox="0 0 40 40"><path fill="#fff" d="M4 20L20 6l16 14h-4v14H8V20z"/><path fill="#1f9be0" d="M16 24h8v10h-8z"/></svg></div>2-4 Units</div>
  <div class="spec" style="left:859px"><div class="ring"><svg width="40" height="40" viewBox="0 0 40 40"><path fill="none" stroke="#fff" stroke-width="3" d="M4 30c8-6 14-6 20-2s10 2 12 0M4 36c8-6 14-6 20-2s10 2 12 0"/><circle cx="26" cy="12" r="5" fill="#fff"/></svg></div>Land</div>
</section>

<h2 class="heading" style="top:2435px"><em>//</em>Our Team</h2>
<div class="pager" style="left:856px;top:2440px"><span class="prev">‹</span><span class="next">›</span><span class="all">View All</span></div>
<div class="member" style="left:160px"><div class="ph" role="img" aria-label="Portrait photo of the company president"></div><h5><span>Colin</span> Brandt</h5><small>President</small></div>
<div class="member pick" style="left:397px"><div class="ph" role="img" aria-label="Portrait photo of the co-founder"></div><h5><span>Nora</span> Vale</h5><small>Co-Founder</small></div>
<div class="member" style="left:620px"><div class="ph" role="img" aria-label="Portrait photo of the managing director"></div><h5><span>Owen</span> Reyes</h5><small>Managing Director</small></div>
<div class="member" style="left:850px"><div class="ph" role="img" aria-label="Portrait photo of the advert manager"></div><h5><span>Derek</span> Hollis</h5><small>Advert Manager</small></div>

<section class="abs news"></section>
<h2 class="heading" style="top:2945px"><em>//</em>Latest Birchwell News</h2>
<div class="pager" style="left:856px;top:2954px"><span class="prev">‹</span><span class="next">›</span><span class="all">View All</span></div>
<article class="story" style="left:160px">
  <div class="ph" role="img" aria-label="Tower completion ceremony outdoors" style="background:linear-gradient(180deg,#a7b7c5,#6f7a6c)"></div>
  <h6>Calloway Hale marks completion of second Kakaako tower</h6>
  <p>The Calloway Hale Corp. on Wednesday marked the completion of the 317-unit Kailo in Honolulu...</p>
</article>
<article class="story pick" style="left:468px">
  <div class="ph" role="img" aria-label="Officials at a press event" style="background:linear-gradient(180deg,#4a5566,#2a2f38)"></div>
  <h6>Tech parent Veridian picks Toronto for first digital neighborhood</h6>
  <p>Streetgrid Labs, the urban innovation unit of tech parent Veridian, and Harborline Toronto plan to foster the...</p>
</article>
<article class="story" style="left:776px">
  <div class="ph" role="img" aria-label="Group of colleagues in an office" style="background:linear-gradient(180deg,#b8a898,#6e6258)"></div>
  <h6>Ashgrove Real Estate channels experience, creativity as it looks to the future</h6>
  <p>The Calloway Hale Corp. on Wednesday marked the completion of the 317-unit Kailo in Honolulu...</p>
</article>
<div class="btn abs" style="left:468px;top:3430px;padding:12px 24px">Read All News
  <svg width="16" height="14" viewBox="0 0 16 14"><path fill="#fff" d="M0 6l16-6-3 14-5-4-2 3V9l7-6-9 5z"/></svg>
</div>

<section class="abs contacts">
  <h2 class="heading light" style="top:60px;left:482px"><em>//</em>Contacts</h2>
  <div class="inp" style="left:258px;top:188px;width:192px">Name</div>
  <div class="inp" style="left:465px;top:188px;width:195px">Email</div>
  <div class="inp" style="left:258px;top:238px;width:192px">Phone No.</div>
  <div class="inp" style="left:465px;top:238px;width:195px">Subject</div>
  <div class="inp" style="left:258px;top:288px;width:402px;height:120px">Message</div>
  <div class="btn abs" style="left:258px;top:425px">Submit
    <svg width="16" height="14" viewBox="0 0 16 14"><path fill="#fff" d="M0 6l16-6-3 14-5-4-2 3V9l7-6-9 5z"/></svg>
  </div>

  <div class="abs" style="left:725px;top:130px;display:flex;align-items:center;gap:10px;color:#c9d3e2;font-weight:700;font-size:38px;letter-spacing:2px"><i style="width:30px;height:30px;background:#c9d3e2;display:block"></i>BIRCHWELL</div>
  <div class="info" style="top:228px;font-size:13px;line-height:1.9"><span>●</span><div>2250 Harlow Ave, Ste 410<br>Los Angeles, CA 90025</div></div>
  <div class="info" style="top:305px;font-size:22px;font-weight:600"><span style="font-size:16px">☏</span>(424) 555-0182</div>
  <div class="info" style="top:350px;font-size:22px;font-weight:600"><span style="font-size:16px">▤</span>(424) 555-0147</div>
  <div class="info" style="top:400px;font-size:13px"><span>✉</span>info@teamdurnio.com</div>
</section>
<div class="abs footline"></div>
<div class="abs copy">© Copyright 2017. Birchwell Holdings. All rights reserved.</div>
<div class="abs fsocial"><i class="dot"></i><i class="dot"></i><i class="dot"></i><i class="dot"></i></div>

</body>
</html>
```